MAXI Fest am Lindenbühl - big party night in Straubing

For a party in the Konrad-Weidinger Halle in Straubing, an attractive poster for "party people" is to be created. The poster should attract at least 3000 visitors. The poster (DIN A 2) will be rebuilt by us for further use as an A5 Flyer and should thus ensure the recognition. There are no special conditions regarding colors and design - but the texts mentioned in the annex must be included. The attached photos can be used in any number and / or in excerpts (we will then insert the original high-resolution files ourselves) Important is the communication: Party Where When A reference to the KVMB as organizer is not welcome (except in the imprint) , Although the party takes place in the context of the KVMB Tri-town tour, the poster should primarily address the general party people. The fans around the rally are coming anyway. Pixel Forge - Description Date: 7th May 2018 Title: MAXI Fest am Lindenbühl am 20. October 2018 possible title signature (optional, also changeable) Halle der Helden! or The hall shakes! or hall tremors with 3,000 party people or hall opening at 7 pm - open end Konrad-Weidinger Halle in Straubing Content (all 5 lines compulsory) • Cult band Gustl and the chrome bumpers • Prairie Town with DJ Rodeo shooting booths • Salon Fortuna with roulette Table • Cult figure Kurvnrutscher • Large season-closing party for the KVMB Dreiländer-Tour Website www.dreilaender-tour-ost.de Imprint: Organizer: KVMB Oberpfalz eV, Kestnerweg 12, 80917 Munich E-Mail: motor@opf.kvmb-verein.de, Tel. : 089 - 7462 308 --------------------------------------------- ------------------------------------------ Colors: Free Format: DIN A2 logos : no font: if it is not a design element we prefer Calibri - but remains free to the designer Additional semicolons to the event (for information only): Saturday: The mega-rally party in the Weidinger-Halle From 18 o'clock hall opening - Our Acts : - Gustl and the chrome bumpers (from 20: 30/21 clock) - Prairie Town in Foyer 2 (award ceremony KVMB eV); then open to all with Rodeo etc. (Markus is checking cooperation with Dakota Ranch) and own DJ - show involvement of Verena as a "good mood" host, especially in the time between 6pm and 9pm: Interviews, Acts or Trials the Western-Arena or the casino etc. - The "small" Auwiesenmarkt with dice, Hau the Luke etc.

Colors

Designer to choose colors to be used in the design.

Requirements

```html
<!DOCTYPE html>
<html lang="en">
<head>
<meta charset="utf-8">
<title>MAXI Fest am Lindenbühl – Konrad-Weidinger Halle Straubing</title>
<link href="https://fonts.googleapis.com/css2?family=Great+Vibes&family=Montserrat:wght@700&family=Open+Sans:wdth,wght@75..100,400..800&display=swap" rel="stylesheet">
<style>
  :root {
    --violet-top: #5b2a8f;
    --violet-deep: #2a1238;
    --night: #120b12;
    --lilac: #c98ff6;
    --lilac-soft: #b887e6;
    --line-violet: #8a3fd6;
    --navy: #2c2f94;
    --white: #ffffff;
    --ink: #000000;
  }
  * { margin: 0; padding: 0; box-sizing: border-box; }
  html, body { width: 838px; height: 1200px; overflow: hidden; background: var(--ink); }
  .poster {
    position: relative; width: 838px; height: 1200px; overflow: hidden;
    font-family: "Open Sans", Calibri, sans-serif; color: var(--white); text-align: center;
  }
  .poster__photo {
    position: absolute; inset: 0;
    background:
      radial-gradient(ellipse 60% 30% at 55% 42%, rgba(120,140,60,.45), transparent 70%),
      radial-gradient(ellipse 50% 25% at 20% 55%, rgba(150,110,40,.35), transparent 70%),
      radial-gradient(ellipse 40% 20% at 75% 70%, rgba(170,40,60,.35), transparent 70%),
      linear-gradient(180deg, var(--violet-top) 0%, var(--violet-deep) 14%, #3a2a22 40%, #2e2418 62%, #1a1410 80%, var(--night) 90%);
  }
  .abs { position: absolute; left: 0; width: 100%; }
  .venue {
    top: 36px; font-family: "Montserrat", sans-serif; font-weight: 700;
    font-size: 32px; line-height: 44px; letter-spacing: .5px;
    text-shadow: 2px 2px 3px rgba(0,0,0,.8);
  }
  .rule { position: absolute; left: 184px; width: 456px; height: 3px;
    background: linear-gradient(90deg, transparent, var(--line-violet) 20%, var(--line-violet) 80%, transparent); }
  .rule--top { top: 130px; }
  .rule--mid { top: 843px; left: 200px; width: 466px; }
  .presents { top: 148px; font-family: "Great Vibes", cursive; font-size: 52px;
    text-shadow: 2px 2px 3px rgba(0,0,0,.7); }
  .title-box { position: absolute; left: 172px; top: 226px; width: 494px; height: 334px;
    border: 2px solid var(--white); }
  .date { top: 236px; font-weight: 700; font-size: 50px; text-shadow: 2px 2px 3px rgba(0,0,0,.8); }
  .headline { font-family: "Montserrat", sans-serif; font-weight: 700; color: var(--lilac);
    text-shadow: -1px -1px 0 #3a1a4a, 1px 1px 0 #3a1a4a, 3px 3px 4px rgba(0,0,0,.8); }
  .headline--main { top: 312px; font-size: 66px; }
  .headline--sub { top: 400px; font-size: 36px; }
  .tagline { top: 470px; font-family: "Great Vibes", cursive; font-size: 52px;
    text-shadow: 2px 2px 3px rgba(0,0,0,.85); }
  .acts { top: 585px; list-style: none; font-weight: 600; font-size: 28px;
    line-height: 41px; font-stretch: 92%; text-shadow: 2px 2px 3px rgba(0,0,0,.8); }
  .opening { top: 866px; font-weight: 800; font-size: 40px; font-stretch: 80%; color: var(--navy);
    text-shadow: -2px -2px 0 var(--white), 2px -2px 0 var(--white), -2px 2px 0 var(--white), 2px 2px 0 var(--white), 3px 4px 5px rgba(0,0,0,.7); }
  .contact { top: 942px; font-weight: 600; font-size: 20px; line-height: 37px;
    text-shadow: 1px 1px 2px rgba(0,0,0,.9); }
  .notes { position: absolute; left: 0; top: 1076px; width: 100%; height: 124px;
    background: var(--night); padding: 8px 42px 0; text-align: left; font-size: 12.6px; line-height: 19.5px; }
  .notes dt { display: inline; color: var(--white); }
  .notes dd { display: inline; color: var(--lilac-soft); }
  .notes p { margin: 0 0 4px; }
  .notes .plain { color: var(--white); }
</style>
</head>
<body>
<main class="poster">
  <div class="poster__photo" role="img" aria-label="Night photo of the glass-fronted Konrad-Weidinger Halle above a dancing crowd under colourful stage lights"></div>

  <h2 class="abs venue">KONRAD-WEIDINGER HALLE<br>IN STRAUBING</h2>
  <div class="rule rule--top"></div>
  <p class="abs presents">Presents</p>

  <div class="title-box"></div>
  <p class="abs date">October 20, 2018</p>
  <h1 class="abs headline headline--main">MAXI FEST</h1>
  <p class="abs headline headline--sub">AM LINDENBÜHL AM</p>
  <p class="abs tagline">Halle der Helden!</p>

  <ul class="abs acts">
    <li>CULT BAND GUSTL AND THE CHROME BUMPERS</li>
    <li>SALON FORTUNA WITH ROULETTE TABLE</li>
    <li>CULT FIGURE KURVNRUTSCHER</li>
    <li>PRAIRIE TOWN WITH DJ RODEO SHOOTING BOOTHS</li>
    <li>LARGE SEASON-CLOSING PARTY FOR THE</li>
    <li>KVMB DREILÄNDER-TOUR</li>
  </ul>
  <div class="rule rule--mid"></div>

  <p class="abs opening">HALL OPENING AT 7 PM</p>

  <div class="abs contact">
    <p>Website: Www.dreilaender-tour-ost.de</p>
    <p>Imprint: Organizer: Kvmb Oberpfalz Ev, Kestnerweg 12, 80917 Munich.</p>
    <p>E-mail: motor@opf.kvmb-verein.de &nbsp;&nbsp;Tel: 089 - 7462 308 ------- -------</p>
  </div>

  <dl class="notes">
    <p><dt>Saturday: </dt><dd>The Mega-rally Party In The Weidinger-halle From 18 O'clock Hall Opening - Hour</dd></p>
    <p><dt>Acts : </dt><dd>Gustl and the chrome bumpers (from 20:30 / 21 Clock) - Prairie Town in Foyer 2 (award ceremony KVMB eV); then open to all with Rodeo etc. (Markus is checking cooperation with Dakota Ranch) and own DJ - show involvement of Verena as a <span class="plain">"good mood"</span> host, especially in the time between <span class="plain">6pm and 9pm</span>: Interviews, Acts or Trials the Western-Arena or the casino etc. - <span class="plain">The "small" Auwiesenmarkt with dice, Hau the Luke etc.</span></dd></p>
  </dl>
</main>
</body>
</html>
```